Cedar Lantern Roots Gathering Music Conference & Concert Series needs a banner design to welco...

We are looking for a banner to use as a backdrop where people can take pictures and promote the event as they upload to social media. The music conference primarily targets high school students so we are looking for a design that will attract a younger audience. The festival revolves around music appreciation in the US/Mexico border. We like the "Cedar LanternRoots Gathering" trumpet logo on the "5th annual" design attached, but we are open to other designs.
Target Market(s)
ages 15-45
Colors
Designer to choose colors to be used in the design.
Look and feel

```html
<!DOCTYPE html>
<html lang="en">
<head>
<meta charset="UTF-8">
<title>Cedar Lantern Roots Gathering — Music Conference &amp; Concert Series</title>
<link rel="stylesheet" href="https://fonts.googleapis.com/css2?family=Anton&family=Bebas+Neue&family=Fredoka:wght@700&display=swap">
<style>
  :root {
    --bg-core: #6c0db4;
    --bg-mid: #3b0f68;
    --bg-edge: #1d0b30;
    --frame-dash: #b53fe3;
    --title-pink: #d24b9e;
    --title-orange: #f7731c;
    --annual-green: #6fc418;
    --subtitle-white: #ffffff;
    --pattern-orange: #f8a12b;
    --pattern-red: #e8413a;
    --art-cyan: #19d3e6;
    --art-magenta: #e52bd8;
    --art-green: #1fc63a;
    --art-yellow: #f6d21c;
  }
  * { margin: 0; padding: 0; box-sizing: border-box; }
  html, body { width: 1200px; height: 958px; overflow: hidden; background: var(--bg-edge); }
  .banner {
    position: relative;
    width: 1200px;
    height: 958px;
    overflow: hidden;
    background: radial-gradient(ellipse 640px 540px at 600px 500px, var(--bg-core) 0%, var(--bg-mid) 50%, var(--bg-edge) 100%);
  }
  .dashed-frame { position: absolute; inset: 0; }

  .edition {
    position: absolute;
    left: 255px; top: 120px;
    font-family: "Fredoka", sans-serif;
    font-weight: 700;
    font-size: 56px;
    line-height: 1;
    color: var(--annual-green);
    letter-spacing: 0.5px;
  }
  .event-name {
    position: absolute;
    left: 0; right: 0; top: 172px;
    text-align: center;
    text-transform: uppercase;
    line-height: 1;
    font-weight: 400;
  }
  .event-name .line-main {
    display: block;
    font-family: "Anton", sans-serif;
    font-size: 112px;
    letter-spacing: -1px;
    padding-left: 10px;
  }
  .event-name .word-pink { color: var(--title-pink); }
  .event-name .word-orange { color: var(--title-orange); }
  .event-name .line-sub {
    display: block;
    font-family: "Fredoka", sans-serif;
    font-weight: 700;
    font-size: 92px;
    color: var(--annual-green);
    letter-spacing: 4px;
    margin-top: 4px;
    padding-left: 10px;
  }
  .tagline {
    position: absolute;
    left: 259px; top: 432px;
    font-family: "Bebas Neue", sans-serif;
    font-size: 55px;
    line-height: 1;
    color: var(--subtitle-white);
    letter-spacing: 0.5px;
    white-space: nowrap;
  }

  .guitar-art {
    position: absolute;
    left: 350px; top: 515px;
    width: 440px; height: 425px;
    border-radius: 220px 220px 0 0;
    background:
      radial-gradient(circle at 50% 76%, rgba(255,255,255,0.22) 0 18%, transparent 30%),
      radial-gradient(circle at 50% 76%, transparent 0 34%, var(--art-green) 35% 37%, transparent 38% 41%, var(--art-cyan) 42% 44%, transparent 46%),
      radial-gradient(circle at 50% 60%, rgba(229,43,216,0.55) 0%, rgba(25,211,230,0.35) 38%, rgba(246,210,28,0.18) 58%, transparent 74%);
  }

  .pattern-strip {
    position: absolute;
    opacity: 0.95;
  }
  .pattern-left, .pattern-right {
    top: 397px; width: 54px; height: 536px;
    background: linear-gradient(180deg, var(--pattern-red), var(--pattern-orange) 25%, var(--pattern-red) 50%, var(--pattern-orange) 75%, var(--pattern-red));
  }
  .pattern-left { left: 26px; }
  .pattern-right { left: 1120px; }
  .pattern-bottom {
    top: 877px; height: 56px;
    background: linear-gradient(90deg, var(--pattern-orange), var(--pattern-red) 33%, var(--pattern-orange) 66%, var(--pattern-red));
  }
  .pattern-bottom-left { left: 80px; width: 360px; }
  .pattern-bottom-right { left: 700px; width: 420px; }
</style>
</head>
<body>
<main class="banner">
  <svg class="dashed-frame" width="1200" height="958" viewBox="0 0 1200 958" aria-hidden="true">
    <rect x="12" y="12" width="1176" height="934" fill="none" stroke="var(--frame-dash)" stroke-width="8" stroke-linecap="round" stroke-dasharray="14 22"/>
  </svg>

  <p class="edition">6TH ANNUAL</p>

  <h1 class="event-name">
    <span class="line-main"><span class="word-pink">Cedar Lantern</span> <span class="word-orange">Roots</span></span>
    <span class="line-sub">Gathering</span>
  </h1>

  <p class="tagline">MUSIC CONFERENCE &amp; CONCERT SERIES</p>

  <div class="guitar-art" role="img" aria-label="Neon line illustration of an electric guitar bursting from a glowing circle with music notes and colourful rays"></div>

  <div class="pattern-strip pattern-left" role="img" aria-label="Vertical folk pattern of orange triangles and red diamonds"></div>
  <div class="pattern-strip pattern-right" role="img" aria-label="Vertical folk pattern of orange triangles and red diamonds"></div>
  <div class="pattern-strip pattern-bottom pattern-bottom-left" role="img" aria-label="Horizontal folk pattern of orange triangles and red diamonds"></div>
  <div class="pattern-strip pattern-bottom pattern-bottom-right" role="img" aria-label="Horizontal folk pattern of orange triangles and red diamonds"></div>
</main>
</body>
</html>
```